Ledgerway Partners, LLC
Project: Biz Card & Stationery
Biz Card & Stationery - Consulting
Biz Card & Stationery
Professional
Denise M. Holloway, CPP, PMP
Founder and CEO
4812 Linwood Avenue NE Suite 210 Atlanta, GA 30318
dholloway@ledgerway-hq.com
ledgerway-hq.com
DUNS No. 052817634 NAICS CODES: 541611 541214 541512 611430 561320

```html
<!DOCTYPE html>
<html lang="en">
<head>
<meta charset="utf-8">
<title>Ledgerway Partners, LLC – Business Card</title>
<link rel="stylesheet" href="https://fonts.googleapis.com/css2?family=Open+Sans:wght@400;600;700&display=swap">
<style>
  :root {
    --page-bg: #e9e6e2;
    --card-white: #ffffff;
    --brand-purple: #7a4fa3;
    --accent-red: #e3262e;
    --ink-black: #1c1c1c;
    --text-dark: #2a2a2a;
    --text-light: #ffffff;
  }
  * { box-sizing: border-box; margin: 0; padding: 0; }
  html, body { width: 1200px; height: 958px; overflow: hidden; }
  body {
    background: var(--page-bg);
    font-family: "Open Sans", Arial, sans-serif;
    position: relative;
  }
  .business-card {
    position: absolute;
    left: 75px; top: 179px;
    width: 1050px; height: 600px;
    background: var(--card-white);
    overflow: hidden;
    box-shadow: 0 6px 24px rgba(0,0,0,0.18);
  }
  .card-swoosh { position: absolute; inset: 0; width: 100%; height: 100%; }
  .brand-lockup {
    position: absolute; left: 70px; top: 78px;
    display: flex; align-items: center; gap: 18px;
  }
  .brand-dot {
    width: 58px; height: 58px; border-radius: 50%;
    background: var(--brand-purple);
  }
  .brand-name {
    font-size: 40px; font-weight: 700; color: var(--brand-purple);
    letter-spacing: 0.5px;
  }
  .holder {
    position: absolute; left: 70px; top: 280px;
  }
  .holder-name {
    font-size: 27px; font-weight: 600; color: var(--brand-purple);
  }
  .holder-title {
    font-size: 25px; font-weight: 400; color: var(--text-dark); margin-top: 4px;
  }
  .contact-list {
    position: absolute; right: 60px; top: 215px;
    list-style: none; text-align: right;
    color: var(--text-light); font-size: 22px; line-height: 1.45;
  }
  .contact-list li { display: flex; justify-content: flex-end; align-items: center; gap: 10px; }
  .contact-list .gap-after { margin-bottom: 10px; }
  .contact-icon { width: 19px; height: 19px; fill: var(--text-light); flex: none; }
</style>
</head>
<body>
  <section class="business-card" aria-label="Business card, front">
    <svg class="card-swoosh" viewBox="0 0 1050 600" preserveAspectRatio="none" aria-hidden="true">
      <path fill="var(--accent-red)" d="M0,462 C220,472 400,440 545,360 L565,395 C500,470 450,540 420,600 L330,600 C250,540 120,505 0,505 Z"/>
      <path fill="var(--brand-purple)" d="M1050,0 L795,0 C715,140 635,270 548,340 C470,405 430,515 412,600 L1050,600 Z"/>
      <path fill="none" stroke="var(--ink-black)" stroke-width="6" d="M0,445 C200,455 400,420 520,330 C600,270 690,140 765,0"/>
    </svg>

    <div class="brand-lockup">
      <span class="brand-dot" aria-hidden="true"></span>
      <span class="brand-name">Ledgerway Partners, LLC</span>
    </div>

    <div class="holder">
      <p class="holder-name">Denise M. Holloway, CPP, PMP</p>
      <p class="holder-title">Founder and CEO</p>
    </div>

    <ul class="contact-list">
      <li>4812 Linwood Avenue NE</li>
      <li>Suite 210</li>
      <li class="gap-after">Atlanta, GA 30318</li>
      <li>404 555 0182
        <svg class="contact-icon" viewBox="0 0 24 24" aria-hidden="true"><path d="M6.6 10.8a15.1 15.1 0 0 0 6.6 6.6l2.2-2.2a1 1 0 0 1 1-.25 11.4 11.4 0 0 0 3.6.57 1 1 0 0 1 1 1V20a1 1 0 0 1-1 1A17 17 0 0 1 3 4a1 1 0 0 1 1-1h3.5a1 1 0 0 1 1 1c0 1.25.2 2.45.57 3.6a1 1 0 0 1-.25 1z"/></svg>
      </li>
      <li class="gap-after">404 555 0197
        <svg class="contact-icon" viewBox="0 0 24 24" aria-hidden="true"><path d="M19 8H5a3 3 0 0 0-3 3v6h4v4h12v-4h4v-6a3 3 0 0 0-3-3zm-3 11H8v-5h8zm3-15H5v3h14z"/></svg>
      </li>
      <li>dholloway@ledgerway-hq.com
        <svg class="contact-icon" viewBox="0 0 24 24" aria-hidden="true"><path d="M20 4H4a2 2 0 0 0-2 2v12a2 2 0 0 0 2 2h16a2 2 0 0 0 2-2V6a2 2 0 0 0-2-2zm0 4-8 5-8-5V6l8 5 8-5z"/></svg>
      </li>
      <li>www.ledgerway-hq.com</li>
    </ul>
  </section>
</body>
</html>
```